Customer Upgrade from Free to Paid Investment Management

Our intent is to have customers that use our free online service consider converting into our paid investment management service.

In current vernacular, we have a Freemium business proposition - but we are just at the early stages of building out our upgrade capabilities.

The design request is detailed in the attached file, but essentially, I'm looking to add another banner to our library. Let me see what you can do!

Target Market(s)

40s-50s, can have any balance in their 401k, at first thought they could manage their 401k themselves, but may be interested in having us manage.

Industry/Entity Type

Investment

Requirements
Must have
• Keep it very simple.
Banner specs are attached in the file
Should not have
• No animation
No "hard sell"

```html
<!DOCTYPE html>
<html lang="en">
<head>
<meta charset="utf-8">
<title>Managed Investing Upgrade Banner</title>
<link rel="stylesheet" href="https://fonts.googleapis.com/css2?family=Arimo:wght@400;700&display=swap">
<style>
  :root {
    --page-bg: #ffffff;
    --banner-top: #f5fbfd;
    --banner-bottom: #d5ebf3;
    --banner-border: #cde2ea;
    --headline: #f07a1f;
    --button-top: #86c66a;
    --button-bottom: #4c9936;
    --button-edge: #3f8a2d;
    --button-text: #ffffff;
    --portrait-light: #c9c4c6;
    --portrait-dark: #6b6e78;
  }
  html, body {
    margin: 0;
    padding: 0;
    width: 1200px;
    height: 236px;
    overflow: hidden;
    background: var(--page-bg);
  }
  .canvas {
    position: relative;
    width: 1200px;
    height: 236px;
  }
  .banner {
    position: absolute;
    left: 39px;
    top: 54px;
    width: 1122px;
    height: 128px;
    box-sizing: border-box;
    border: 1.5px solid var(--banner-border);
    border-radius: 7px;
    background: linear-gradient(to bottom, var(--banner-top), var(--banner-bottom));
  }
  .advisor-portrait {
    position: absolute;
    left: 57px;
    top: 16px;
    width: 190px;
    height: 166px;
    border-radius: 80px 80px 0 0;
    background: linear-gradient(to bottom, var(--portrait-light) 0%, #a99a94 45%, var(--portrait-dark) 100%);
  }
  .headline {
    position: absolute;
    left: 252px;
    top: 100px;
    margin: 0;
    font-family: "Arimo", Arial, sans-serif;
    font-weight: 700;
    font-size: 29.5px;
    line-height: 36px;
    color: var(--headline);
  }
  .learn-more {
    position: absolute;
    left: 960px;
    top: 97px;
    width: 186px;
    height: 46px;
    text-decoration: none;
  }
  .learn-more svg {
    position: absolute;
    inset: 0;
  }
  .learn-more span {
    position: absolute;
    left: 0;
    width: 168px;
    top: 0;
    line-height: 46px;
    text-align: center;
    font-family: "Arimo", Arial, sans-serif;
    font-weight: 700;
    font-size: 23px;
    color: var(--button-text);
    text-shadow: 0 1px 2px rgba(20, 50, 10, 0.85);
  }
</style>
</head>
<body>
  <div class="canvas">
    <div class="banner"></div>
    <div class="advisor-portrait" role="img" aria-label="Portrait of a smiling investment advisor in a grey blazer"></div>
    <p class="headline">Want us to manage this for you?</p>
    <a class="learn-more" href="#">
      <svg width="186" height="46" viewBox="0 0 186 46" aria-hidden="true">
        <defs>
          <linearGradient id="buttonFill" x1="0" y1="0" x2="0" y2="1">
            <stop offset="0" stop-color="var(--button-top)"/>
            <stop offset="1" stop-color="var(--button-bottom)"/>
          </linearGradient>
        </defs>
        <path d="M5 1 H165 L184 23 L165 45 H5 Q1 45 1 41 V5 Q1 1 5 1 Z"
              fill="url(#buttonFill)" stroke="var(--button-edge)" stroke-width="1.5"/>
      </svg>
      <span>Learn more</span>
    </a>
  </div>
</body>
</html>
```